Mistholm Consulting Business

** Please add the content information from my old business card
1. I would like to see a two sided business card with both options with the 1st Option--Sketch Forge-new WHITE BACKGROUND LOGO
2 nd Option-Sketch Forge - new BLACK- Background Logo
3rd -Option a business card with my Photo on the card
Please add the new word to the card information:
EXECUTION
AS THE OWNER'S REP
WE AIM TO ACHIEVE YOUR
INFRASTRUCTURE VISION with
OUR SPECIALIZATION & EXECUTION in:

FUNDING Planning
BUSINESS Planning
INFRASTRUCTURE Planning
PROJECT Management
Since 2012
_____________________________________________________________________
I want to get spot uv raised printing. I was liking a a nice rich white linen paper stock with black writing & NOT A COLORED CARD other than a variety of white or black cards concept

```html
<!DOCTYPE html>
<html lang="en">
<head>
<meta charset="utf-8">
<title>Mistholm Consulting – Business Card</title>
<link href="https://fonts.googleapis.com/css2?family=Arimo:wght@400;700&display=swap" rel="stylesheet">
<style>
  :root {
    --backdrop: #e4e4e2;
    --card: #2f2e33;
    --card-deep: #27262b;
    --white: #ffffff;
    --red: #e0161e;
    --muted: #48474d;
  }
  * { margin: 0; padding: 0; box-sizing: border-box; }
  html, body { width: 1200px; height: 801px; overflow: hidden; }
  body {
    background: var(--backdrop);
    font-family: "Arimo", Arial, sans-serif;
    color: var(--white);
    position: relative;
  }
  .card {
    position: absolute;
    width: 540px;
    height: 309px;
    background: var(--card);
    border-bottom: 4px solid var(--red);
    box-shadow: 0 6px 18px rgba(0,0,0,.22);
    overflow: hidden;
  }
  .card-front { left: 30px; top: 246px; }
  .card-back  { left: 630px; top: 246px; }

  .brand { position: absolute; text-align: right; }
  .brand-name {
    font-weight: 700;
    font-size: 42px;
    letter-spacing: -1px;
    line-height: 1;
    color: var(--white);
  }
  .brand-name::after {
    content: "";
    display: inline-block;
    width: 10px; height: 10px;
    background: var(--red);
    margin-left: 6px;
    vertical-align: top;
  }
  .brand-tag {
    font-size: 10px;
    letter-spacing: 11px;
    margin-top: 6px;
    margin-right: -11px;
  }
  .card-front .brand { right: 34px; top: 40px; }
  .card-back .brand { right: 26px; top: 22px; }

  .rule { position: absolute; height: 1px; background: var(--red); }

  .locations {
    position: absolute; right: 34px; top: 168px;
    font-size: 14px; line-height: 1.4; text-align: right;
  }
  .person { position: absolute; left: 36px; top: 182px; }
  .person-name { color: var(--red); font-weight: 700; font-size: 19px; }
  .person-role { font-size: 13px; margin-top: 3px; }
  .contacts {
    position: absolute; left: 36px; top: 244px;
    list-style: none; font-size: 13px; line-height: 19px;
  }
  .contacts li { display: flex; align-items: center; gap: 9px; }
  .contacts svg { width: 12px; height: 12px; flex: none; }

  .pitch {
    position: absolute; right: 26px; top: 82px;
    text-align: right; font-size: 12.5px; line-height: 15px;
    text-transform: none;
  }
  .pitch .accent { color: var(--red); font-weight: 700; }
  .services {
    position: absolute; right: 26px; top: 170px;
    list-style: none; text-align: right; font-size: 12.5px; line-height: 16px;
  }
  .services li::after {
    content: ""; display: inline-block; width: 7px; height: 7px;
    background: var(--red); margin-left: 7px; vertical-align: 1px;
  }
  .since {
    position: absolute; right: 26px; bottom: 20px;
    background: var(--red); color: var(--white);
    font-size: 14px; padding: 4px 14px 4px 20px;
    clip-path: polygon(12px 0, 100% 0, 100% 100%, 12px 100%, 0 50%);
  }
  .mark-area {
    position: absolute; left: 0; bottom: 0; width: 250px; height: 150px;
    background: linear-gradient(135deg, var(--card) 0%, var(--muted) 55%, var(--card-deep) 100%);
    opacity: .7;
  }
</style>
</head>
<body>

  <section class="card card-front" aria-label="Card front">
    <div class="brand">
      <div class="brand-name">Mistholm</div>
      <div class="brand-tag">CONSULTING</div>
    </div>
    <div class="rule" style="left:36px; right:34px; top:118px;"></div>
    <div class="locations">Northvale NT<br>Harrowgate NB</div>

    <div class="person">
      <div class="person-name">Dana Whitcombe-Ravel</div>
      <div class="person-role">CEO / Lead Project Manager</div>
    </div>
    <div class="rule" style="left:36px; width:220px; top:232px;"></div>
    <ul class="contacts">
      <li><svg viewBox="0 0 12 12"><path d="M2.5 1h2l1 3-1.4 1a6 6 0 0 0 3 3l1-1.4 3 1v2A1 1 0 0 1 10 11 9 9 0 0 1 1 2a1 1 0 0 1 1.5-1z" fill="none" stroke="#e0161e" stroke-width="1.1"/></svg>867.555.0142</li>
      <li><svg viewBox="0 0 12 12"><rect x="1" y="2.5" width="10" height="7" fill="none" stroke="#e0161e" stroke-width="1.1"/><path d="M1 2.5l5 4 5-4" fill="none" stroke="#e0161e" stroke-width="1.1"/></svg>dana@mistholm.ca</li>
      <li><svg viewBox="0 0 12 12"><circle cx="6" cy="6" r="5" fill="none" stroke="#e0161e" stroke-width="1.1"/><path d="M1 6h10M6 1c-3 3-3 7 0 10M6 1c3 3 3 7 0 10" fill="none" stroke="#e0161e" stroke-width=".9"/></svg>www.mistholm.ca</li>
    </ul>
  </section>

  <section class="card card-back" aria-label="Card back">
    <div class="mark-area" role="img" aria-label="Large faint embossed brand mark decoration"></div>
    <div class="brand">
      <div class="brand-name">Mistholm</div>
      <div class="brand-tag">CONSULTING</div>
    </div>
    <p class="pitch">
      EXECUTION<br>
      AS THE <span class="accent">OWNER'S REP</span><br>
      WE AIM TO ACHIEVE YOUR<br>
      INFRASTRUCTURE VISION with<br>
      OUR SPECIALIZATION &amp; EXECUTION in:
    </p>
    <div class="rule" style="left:210px; right:26px; top:164px;"></div>
    <ul class="services">
      <li>FUNDING Planning</li>
      <li>BUSINESS Planning</li>
      <li>INFRASTRUCTURE Planning</li>
      <li>PROJECT Management</li>
    </ul>
    <div class="rule" style="left:270px; width:130px; bottom:34px;"></div>
    <div class="since">Since 2012</div>
  </section>

</body>
</html>
```